Letterhead Design Project

Need Letterhead and Envelpe design with One Single or Both Side pockets for a yong dynamic employee friendly IT services company. It should be professional and sleek and should look fresh.

Target Market(s)

IT Corporate

Industry/Entity Type

It Company

```html
<!DOCTYPE html>
<html lang="en">
<head>
<meta charset="utf-8">
<title>Kelvora Technologies – Letterhead</title>
<link href="https://fonts.googleapis.com/css2?family=Open+Sans:wght@400;600;700&display=swap" rel="stylesheet">
<style>
  :root {
    --backdrop: #1c1c1c;
    --paper: #ffffff;
    --brand-red: #c8202f;
    --ink: #4a4a4a;
    --ink-strong: #2e2e2e;
    --ink-soft: #6b6b6b;
    --signature-tone: #d9d9d9;
  }
  * { box-sizing: border-box; margin: 0; padding: 0; }
  html, body {
    width: 1200px;
    height: 1024px;
    overflow: hidden;
    background: var(--backdrop);
    font-family: "Open Sans", Arial, sans-serif;
  }
  .canvas {
    position: relative;
    width: 1200px;
    height: 1024px;
  }
  .letterhead {
    position: absolute;
    left: 250px;
    top: 20px;
    width: 700px;
    height: 984px;
    background: var(--paper);
    padding: 64px 64px 0 64px;
    color: var(--ink);
  }
  .brand {
    display: flex;
    align-items: center;
    gap: 8px;
    color: var(--brand-red);
    font-weight: 700;
    font-size: 22px;
    letter-spacing: 0.5px;
    line-height: 1;
  }
  .brand-dot {
    width: 12px;
    height: 12px;
    background: var(--brand-red);
    border-radius: 50%;
  }
  .letter {
    margin-top: 62px;
    font-size: 11.5px;
    line-height: 1.55;
  }
  .letter-date, .letter-greeting { margin-bottom: 6px; }
  .letter-paragraph { margin-bottom: 14px; }
  .signature {
    width: 110px;
    height: 22px;
    margin-top: 10px;
    background: linear-gradient(90deg, var(--signature-tone), #eeeeee);
    border-radius: 3px;
  }
  .signatory-title {
    margin-top: 4px;
    font-weight: 700;
    color: var(--ink-strong);
  }
  .footer {
    position: absolute;
    left: 64px;
    right: 64px;
    bottom: 70px;
  }
  .footer-rule {
    height: 1.5px;
    background: var(--brand-red);
  }
  .footer-details {
    display: flex;
    justify-content: space-between;
    align-items: flex-start;
    padding: 14px 0 18px;
    font-size: 9.5px;
    line-height: 1.5;
    color: var(--ink-soft);
  }
  .contact-item {
    display: flex;
    gap: 5px;
    align-items: flex-start;
  }
  .contact-item svg {
    flex: none;
    width: 10px;
    height: 10px;
    margin-top: 2px;
    fill: var(--brand-red);
  }
  .contact-stack { display: flex; flex-direction: column; gap: 1px; }
  .web-accent { color: var(--brand-red); }
</style>
</head>
<body>
<div class="canvas">
  <article class="letterhead">
    <header class="brand">
      <span class="brand-dot"></span>
      <span class="brand-name">kelvora technologies</span>
    </header>

    <section class="letter">
      <p class="letter-date">May/08/2014</p>
      <p class="letter-greeting">Dear Peter,</p>
      <p class="letter-paragraph">Lorem ipsum is simply placeholder text used across the printing and typesetting trade. It has served as the standard filler for many years, ever since early printers arranged rows of type to build sample pages. It has lasted through many changes in the craft, including the move to electronic layout, and remains essentially unchanged. It became common on printed sample sheets, and more recently in page layout software that ships with ready-made versions of it for every new document.</p>
      <p class="letter-paragraph">Contrary to popular belief, lorem ipsum is not simply random text. It grew out of an old passage of classical writing, which makes it far older than most people expect. Scholars who studied the unusual words in it traced them back through many old manuscripts and compared every use they could find, until they arrived at a likely source. The passage comes from a long essay on the nature of pleasure and pain, a text that was widely read and discussed for centuries by students and teachers alike. The familiar opening line, "Lorem ipsum dolor sit amet..", comes from one of its early sections.</p>
      <p class="letter-paragraph">The standard block of lorem ipsum in use for many years is reproduced below for those interested. The matching sections of the original essay are also shown in their exact form, together with a plain English translation prepared for modern readers.</p>
      <p class="letter-paragraph">It is a long established fact that a reader will be distracted by the readable content of a page when looking at its layout. The point of using lorem ipsum is that it has a more-or-less normal distribution of letters, as opposed to using 'Content here, content here', making it look like readable English. Many desktop publishing packages and web page editors now use lorem ipsum as their default model text, and a search for 'lorem ipsum' will uncover many web sites still in their infancy. Various versions have evolved over the years, sometimes by accident, sometimes on purpose (injected humour and the like).</p>

      <div class="signature" role="img" aria-label="Handwritten signature of Marcus Hale"></div>
      <p class="signatory-title">Company Director</p>
    </section>

    <footer class="footer">
      <div class="footer-rule"></div>
      <div class="footer-details">
        <div class="contact-item">
          <svg viewBox="0 0 10 10"><path d="M5 0a3.5 3.5 0 0 0-3.5 3.5C1.5 6 5 10 5 10s3.5-4 3.5-6.5A3.5 3.5 0 0 0 5 0zm0 4.8a1.3 1.3 0 1 1 0-2.6 1.3 1.3 0 0 1 0 2.6z"/></svg>
          <span>48 W. Orchard Lane,<br>Riverton, CA 90210</span>
        </div>
        <div class="contact-item">
          <svg viewBox="0 0 10 10"><path d="M5 0a3.5 3.5 0 0 0-3.5 3.5C1.5 6 5 10 5 10s3.5-4 3.5-6.5A3.5 3.5 0 0 0 5 0zm0 4.8a1.3 1.3 0 1 1 0-2.6 1.3 1.3 0 0 1 0 2.6z"/></svg>
          <span>Level 3, Cedar Point No-212,<br>Tech Park Zone, Eastfield Pune – 411014</span>
        </div>
        <div class="contact-stack">
          <div class="contact-item">
            <svg viewBox="0 0 10 10"><path d="M2 0.5l1.6 2.2-1 1a6 6 0 0 0 3.7 3.7l1-1L9.5 8 8.3 9.5C4.2 9.5 0.5 5.8 0.5 1.7z"/></svg>
            <span>555.204.7310</span>
          </div>
          <div class="contact-item">
            <svg viewBox="0 0 10 10"><path d="M0.5 2h9v6h-9z M0.5 2l4.5 3.5L9.5 2" fill="none" stroke="#c8202f" stroke-width="1"/></svg>
            <span>info@kelvoratech.com</span>
          </div>
        </div>
        <div class="contact-item">
          <svg viewBox="0 0 10 10"><circle cx="5" cy="5" r="4.3" fill="none" stroke="#c8202f" stroke-width="1"/><path d="M0.7 5h8.6M5 0.7c-2.4 2.4-2.4 6.2 0 8.6M5 0.7c2.4 2.4 2.4 6.2 0 8.6" fill="none" stroke="#c8202f" stroke-width="0.8"/></svg>
          <span>www.<span class="web-accent">kelvoratech</span>.com</span>
        </div>
      </div>
      <div class="footer-rule"></div>
    </footer>
  </article>
</div>
</body>
</html>
```